Portrait Photographer Newsletter (www.lakesidelensworks.com)

We would like a newsletter that can be used in Mailbright Hub....you can visit our website to get some content....The main topics for the newsletter are 1. planning for your family portraits 2. We also offer restoration of your family heirlooms 3. Coming Soon.....www.dockandcottageguard.com (get content off our website.)
Misc:
Gift Certificates are available.
Click to schedule you appt today.
Mothers day.
I can provide more pictures but we really need the content of the news letter- we need a good writer...feel free to use info our of our website or be creative :)
We need help keeping up with email marketing if we find a fit, we would like to use find someone to help with this weekly or monthly
Target Market(s)
Family, middle to upper class
Industry/Entity Type
Portrait Photography
Designer to choose colors to be used in the design.

```html
<!DOCTYPE html>
<html lang="en">
<head>
<meta charset="utf-8">
<title>Dock &amp; Cottage Guard – Newsletter</title>
<link rel="stylesheet" href="https://fonts.googleapis.com/css2?family=Montserrat:wght@600;700;800&family=Oswald:wght@500;600&family=Roboto+Condensed:wght@400;700&display=swap">
<style>
  :root{
    --navy:#1f2358;
    --blue:#1e9fe0;
    --blue-light:#5cc3f0;
    --ink:#2b2b2b;
    --paper:#ffffff;
    --stage:#dcdcdc;
  }
  *{box-sizing:border-box;margin:0;padding:0}
  html,body{width:1200px;height:674px;overflow:hidden;background:var(--stage)}
  .newsletter{
    position:absolute;left:374px;top:17px;width:502px;height:712px;
    background:var(--paper);transform:scale(0.899);transform-origin:0 0;
    box-shadow:0 6px 18px rgba(0,0,0,.25);overflow:hidden;
    font-family:"Roboto Condensed",Arial,sans-serif;color:var(--ink);
  }
  .masthead{position:absolute;left:0;top:0;width:502px;height:115px}
  .masthead svg{position:absolute;inset:0}
  .brand{position:absolute;left:155px;top:18px;display:flex;align-items:center;gap:10px}
  .brand-name{font-family:"Montserrat",sans-serif;font-weight:800;color:var(--blue);font-size:17px;line-height:18px;text-align:center;letter-spacing:.5px}
  .brand-mark{width:46px;height:46px;border-radius:50%;border:7px solid var(--blue);background:#fff}
  .photo{position:absolute;top:120px;height:257px}
  .photo-estate{left:0;width:247px;background:linear-gradient(180deg,#5f86b8 0%,#8fa8c8 35%,#d8c3a0 62%,#6f6a5a 80%,#3f6a2e 100%)}
  .photo-family{left:256px;width:246px;background:linear-gradient(90deg,#9a1f24 0%,#b8272c 45%,#e9e5df 70%,#c7c2bb 100%)}
  .services-bar{position:absolute;left:0;top:340px;width:502px;height:37px;background:rgba(35,35,40,.78);
    font-family:"Montserrat",sans-serif;font-weight:700;font-size:18.5px;color:#fff;text-align:center;line-height:37px}
  .services-bar span{color:var(--blue)}
  .intro{position:absolute;left:20px;top:395px;width:215px;font-size:9.6px;line-height:14.3px;text-align:justify;hyphens:auto}
  .intro b{font-weight:700}
  .gift-title{position:absolute;left:20px;top:530px;font-family:"Montserrat",sans-serif;font-weight:800;font-size:19.5px;color:var(--navy)}
  .gift-are{position:absolute;left:14px;top:556px;width:50px;height:22px;transform:rotate(-90deg) translate(-50px,0);transform-origin:0 0;
    font-family:"Oswald",sans-serif;font-weight:600;font-size:21px;line-height:22px;color:var(--navy);letter-spacing:1px}
  .gift-available{position:absolute;left:42px;top:545px;font-family:"Oswald",sans-serif;font-weight:600;font-size:50px;line-height:58px;color:var(--blue);transform:scaleX(.82);transform-origin:0 0}
  .schedule-btn{position:absolute;left:20px;top:613px;width:215px;height:34px;border-radius:17px;
    background:linear-gradient(180deg,#3ab7f0,#1386c9);box-shadow:0 2px 4px rgba(0,0,0,.3);
    font-family:"Oswald",sans-serif;font-weight:500;font-size:11.5px;color:#fff;line-height:34px;padding-left:38px}
  .schedule-btn svg{position:absolute;left:5px;top:5px}
  .topic{position:absolute;left:262px;display:flex;gap:8px;font-family:"Montserrat",sans-serif;font-weight:600;font-size:13.5px;line-height:16px;color:var(--navy)}
  .topic-dot{flex:none;width:26px;height:26px;border-radius:50%;border:5px solid var(--blue);background:#fff;margin-top:2px}
  .topic-plan{top:398px}
  .topic-restore{top:445px}
  .coming-soon{position:absolute;left:264px;top:488px;font-family:"Montserrat",sans-serif;font-weight:800;font-size:21px;color:var(--blue);letter-spacing:.3px}
  .preview{position:absolute;top:525px;width:68px;height:68px;border-radius:50%;border:3px solid #e6e6e6;box-shadow:0 1px 3px rgba(0,0,0,.35)}
  .preview-1{left:262px;background:linear-gradient(180deg,#9fb7c8,#6d8a5a 70%,#c9b999)}
  .preview-2{left:340px;background:linear-gradient(180deg,#b7c9d3,#7d9c6a 65%,#d6cdb8)}
  .preview-3{left:418px;background:linear-gradient(180deg,#8fb5d8,#c9d9e6 55%,#e2d5bd)}
  .social-box{position:absolute;left:265px;top:615px;width:110px;height:32px;border-radius:3px;
    background:linear-gradient(180deg,#5a78b8,#3b5a9a);display:flex;align-items:center;gap:8px;padding-left:10px;color:#fff}
  .social-box .square{width:14px;height:14px;background:#fff;opacity:.9}
  .social-box p{font-family:"Montserrat",sans-serif;font-weight:700;font-size:10px;line-height:11px}
  .social-box small{display:block;font-weight:600;font-size:7px}
  .partner{position:absolute;left:390px;top:615px;width:105px;text-align:center}
  .partner-name{font-family:"Montserrat",sans-serif;font-weight:700;font-size:12px;line-height:13px;color:var(--navy)}
  .partner-tag{font-size:5px;color:#555;letter-spacing:.3px;margin-top:3px}
  .contact-bar{position:absolute;left:0;top:668px;width:502px;height:44px;background:var(--navy);color:#fff;
    font-family:"Oswald",sans-serif;font-weight:500;font-size:11.5px}
  .contact-item{position:absolute;top:14px;text-align:center;white-space:nowrap}
  .contact-item .icon{position:absolute;left:50%;top:-24px;margin-left:-9px;width:18px;height:18px;border-radius:50%;background:var(--blue)}
  .contact-item .icon svg{display:block;margin:3px auto 0}
  .contact-address{left:22px}
  .contact-phone{left:203px}
  .contact-web{left:330px}
</style>
</head>
<body>
<article class="newsletter">
  <header class="masthead">
    <svg width="502" height="115" viewBox="0 0 502 115">
      <defs>
        <linearGradient id="band" x1="0" x2="1">
          <stop offset="0" stop-color="#2aa7e2"/><stop offset="1" stop-color="#1b8fd2"/>
        </linearGradient>
      </defs>
      <rect width="502" height="115" fill="#f3f3f3"/>
      <polygon points="0,0 32,0 80,70 0,70" fill="#cfe8f6"/>
      <polygon points="52,0 98,0 142,82 104,82" fill="var(--navy)"/>
      <polygon points="420,17 502,17 502,30 412,30" fill="var(--navy)"/>
      <polygon points="397,32 502,32 502,72 380,72" fill="url(#band)"/>
      <polygon points="470,5 502,5 502,14 466,14" fill="#cfe8f6"/>
      <rect x="0" y="82" width="502" height="33" fill="url(#band)"/>
      <rect x="0" y="112" width="502" height="3" fill="#fff"/>
    </svg>
    <div class="brand">
      <div class="brand-name">DOCK &amp; COTTAGE<br>GUARD</div>
      <div class="brand-mark"></div>
    </div>
  </header>

  <div class="photo photo-estate" role="img" aria-label="Photo of a large lit coastal house at dusk with a brick driveway"></div>
  <div class="photo photo-family" role="img" aria-label="Photo of a family of three posing beside a red ship hull with ropes"></div>
  <h1 class="services-bar"><span>DOCK &amp; COTTAGE</span> GUARD SERVICES</h1>

  <p class="intro"><b>Dock and Cottage Guard</b> is a trustworthy service that visits and visually inspects property and vessels to check on their well-being and notifies the owner of its status. If a situation does occur, you can be assured we will notify you as soon as possible and help handle it to minimize further damage and resolve the problem. We watch along the Mid-Atlantic area in Harbor Point and Millbrook in Tidewater County, Delaware, USA.</p>

  <h2 class="gift-title">GIFT CERTIFICATES</h2>
  <div class="gift-are">ARE</div>
  <div class="gift-available">AVAILABLE</div>

  <div class="schedule-btn">
    <svg width="24" height="24" viewBox="0 0 24 24"><circle cx="12" cy="12" r="12" fill="#fff"/><path d="M6 10h6V6l7 6-7 6v-4H6z" fill="var(--navy)"/></svg>
    CLICK TO SCHEDULE YOU APPT TODAY.
  </div>

  <div class="topic topic-plan"><span class="topic-dot"></span><p>Planning for your family<br>portraits.</p></div>
  <div class="topic topic-restore"><span class="topic-dot"></span><p>We also offer restoration<br>of your family heirlooms.</p></div>
  <h2 class="coming-soon">COMING SOON.....</h2>

  <div class="preview preview-1" role="img" aria-label="Portrait of a child at the beach"></div>
  <div class="preview preview-2" role="img" aria-label="Portrait of a girl among dune grass"></div>
  <div class="preview preview-3" role="img" aria-label="Portrait of a toddler by the sea"></div>

  <div class="social-box"><span class="square"></span><p><small>Like us on</small>Circlepage</p></div>
  <div class="partner">
    <div class="partner-name">Lakeside Lensworks</div>
    <div class="partner-tag">Artistic portraits &amp; family heirlooms</div>
  </div>

  <footer class="contact-bar">
    <div class="contact-item contact-address">
      <span class="icon"><svg width="8" height="11" viewBox="0 0 8 11"><path d="M4 0a4 4 0 0 1 4 4c0 3-4 7-4 7S0 7 0 4a4 4 0 0 1 4-4z" fill="#fff"/><circle cx="4" cy="4" r="1.5" fill="var(--blue)"/></svg></span>
      Harbor Point, DE 19900
    </div>
    <div class="contact-item contact-phone">
      <span class="icon"><svg width="10" height="10" viewBox="0 0 10 10"><path d="M2 0l2 2.5-1.2 1.3a6 6 0 0 0 3.4 3.4L7.5 6 10 8l-1.5 2C4 10 0 6 0 1.5z" fill="#fff"/></svg></span>
      555-014-2290
    </div>
    <div class="contact-item contact-web">
      <span class="icon"><svg width="10" height="10" viewBox="0 0 10 10"><circle cx="5" cy="5" r="4.3" fill="none" stroke="#fff" stroke-width="1.2"/><path d="M0.7 5h8.6M5 0.7c2.5 2.5 2.5 6.1 0 8.6M5 0.7c-2.5 2.5-2.5 6.1 0 8.6" fill="none" stroke="#fff" stroke-width=".9"/></svg></span>
      www.dockandcottageguard.com
    </div>
  </footer>
</article>
</body>
</html>
```